Pest Control Company needs business card!

Hi there, we need a business card designed for our new Pest Control Company. Ideally this card will be simple, yet feel elegant and high end. We want to use the colours Orange, Black and White. Please see our attached logo for the exact colours.

Business card details:

Phone - 0461 275 804
Name - Gavin Holloway
Email - Info@steadfastverminguard.com.au

We would also like to include the following list with dot points:

SERVICES / INSPECTIONS

Termites, Wood Borers, Ants, Cockroaches, Spiders, Fleas, Mice, Rats, Bed Bugs, & More!

```html
<!DOCTYPE html>
<html lang="en">
<head>
<meta charset="utf-8">
<title>Steadfast Vermin Guard – Business Card</title>
<link rel="stylesheet" href="https://fonts.googleapis.com/css2?family=Montserrat:wght@400;500;600;800&display=swap">
<style>
  :root {
    --stage: #1c1c1c;
    --card-black: #0a0a0a;
    --card-edge: #1e1e1e;
    --orange: #f5821f;
    --white: #ffffff;
    --red: #e3262b;
  }
  * { box-sizing: border-box; margin: 0; padding: 0; }
  html, body { width: 1200px; height: 780px; overflow: hidden; }
  body {
    background: var(--stage);
    font-family: "Montserrat", Arial, sans-serif;
    color: var(--white);
    position: relative;
  }
  .card {
    position: absolute;
    width: 560px;
    height: 320px;
    background: radial-gradient(ellipse at 45% 35%, var(--card-edge), var(--card-black) 70%);
    box-shadow: 0 18px 40px rgba(0,0,0,.6);
    overflow: hidden;
  }
  .card--front { left: 40px; top: 70px; }
  .card--back { left: 600px; top: 390px; }

  /* Front */
  .brand {
    position: absolute;
    left: 0; right: 0; top: 58px;
    display: flex; align-items: center; justify-content: center; gap: 14px;
  }
  .brand__name {
    font-weight: 800;
    font-size: 30px;
    line-height: 1.02;
    text-transform: uppercase;
    color: var(--white);
    text-align: right;
  }
  .brand__mark {
    width: 72px; height: 72px;
    border-radius: 50%;
    background: var(--orange);
  }
  .divider {
    position: absolute;
    left: 48px; right: 48px; top: 196px;
    height: 1px; background: var(--white);
  }
  .services__label {
    position: absolute;
    left: 0; right: 0; top: 172px;
    text-align: center;
    font-size: 8px;
    letter-spacing: 5px;
    color: var(--orange);
    text-transform: uppercase;
  }
  .services__list {
    position: absolute;
    left: 0; right: 0; top: 214px;
    text-align: center;
    font-weight: 500;
    font-size: 14px;
    line-height: 24px;
    text-transform: uppercase;
  }
  .services__sep { color: var(--orange); padding: 0 5px; }

  /* Back */
  .mascot-area {
    position: absolute;
    right: -30px; top: -30px;
    width: 290px; height: 290px;
    border-radius: 50%;
    background: radial-gradient(circle at 45% 45%, var(--orange) 55%, rgba(245,130,31,0) 72%);
  }
  .person { position: absolute; left: 40px; top: 128px; }
  .person__name {
    font-weight: 800;
    font-size: 30px;
    text-transform: uppercase;
    letter-spacing: .5px;
  }
  .person__first { color: var(--orange); }
  .person__last { color: var(--white); }
  .person__role { font-size: 15px; font-weight: 500; margin-top: 4px; }
  .contact { position: absolute; left: 40px; bottom: 34px; list-style: none; }
  .contact__item {
    display: flex; align-items: center; gap: 10px;
    font-size: 15px; font-weight: 500; margin-top: 10px;
  }
  .contact__icon { width: 24px; height: 24px; flex: none; }
</style>
</head>
<body>
  <section class="card card--front" aria-label="Business card front">
    <div class="brand">
      <p class="brand__name">Steadfast<br>Vermin<br>Guard</p>
      <span class="brand__mark" aria-hidden="true"></span>
    </div>
    <p class="services__label">Services / Inspections</p>
    <div class="divider"></div>
    <p class="services__list">
      Wood<span class="services__sep">|</span>Borers<span class="services__sep">|</span>Ants<span class="services__sep">|</span>Cockroaches<span class="services__sep">|</span>Spiders Fleas,<br>
      Mice<span class="services__sep">|</span>Rats<span class="services__sep">|</span>Bed Bugs<span class="services__sep">|</span>&amp; More!
    </p>
  </section>

  <section class="card card--back" aria-label="Business card back">
    <div class="mascot-area" role="img" aria-label="Large orange bug mascot illustration"></div>
    <div class="person">
      <p class="person__name"><span class="person__first">Gavin</span> <span class="person__last">Holloway</span></p>
      <p class="person__role">Managing Director</p>
    </div>
    <ul class="contact">
      <li class="contact__item">
        <svg class="contact__icon" viewBox="0 0 24 24" aria-hidden="true">
          <circle cx="12" cy="12" r="11" fill="none" stroke="var(--orange)" stroke-width="1.6"/>
          <path d="M8 7.5c.6-.6 1.4-.5 1.8.1l.9 1.5c.3.5.2 1.1-.2 1.4l-.6.5c.6 1.3 1.6 2.3 2.9 2.9l.5-.6c.4-.4 1-.5 1.4-.2l1.5.9c.6.4.7 1.2.1 1.8-1 1-2.5 1.2-3.8.5-2.2-1.2-4-3-5.2-5.2-.7-1.3-.5-2.8.5-3.8z" fill="var(--orange)"/>
        </svg>
        0461 275 804
      </li>
      <li class="contact__item">
        <svg class="contact__icon" viewBox="0 0 24 24" aria-hidden="true">
          <circle cx="12" cy="12" r="11" fill="none" stroke="var(--orange)" stroke-width="1.6"/>
          <rect x="6.5" y="8" width="11" height="8" fill="var(--orange)"/>
          <path d="M6.5 8l5.5 4.5L17.5 8" fill="none" stroke="var(--card-black)" stroke-width="1"/>
        </svg>
        Info@steadfastverminguard.com.au
      </li>
    </ul>
  </section>
</body>
</html>
```